Graffiti removal company needs cool flyer

Beacon Rinse & Spray is a pressure washing company based in Alberta, Canada - we offer general power washing and graffiti removal services for residential & commercial properties. . We would like an edgy/cool 2 sided flyer created to hand out to business / possible door hanger style with specific focus on graffiti removal but also touching on the power washing we can provide. The flyer should have the added pictures (use some before & afters) & wording attached. The picture from Harlow Dome should be used as its a prominent sports arena. There should be some graffiti fonts used to convey the titles/ steps/headings but the look should be clean.
Contact info to appear on flyer
Company logo
Ph 780-555-0143
derek@beaconrinse.ca
www.beaconrinseandspray.ca

```html
<!DOCTYPE html>
<html lang="en">
<head>
<meta charset="utf-8">
<title>Beacon Rinse &amp; Spray – Graffiti Removal Door Hanger</title>
<link href="https://fonts.googleapis.com/css2?family=Montserrat:wght@400;600;700&family=Poppins:wght@600;700&family=Sedgwick+Ave+Display&display=swap" rel="stylesheet">
<style>
  :root{
    --navy:#0d2a4f;
    --orange:#f36f16;
    --white:#ffffff;
    --ink:#2a2f38;
    --panel:#efeff1;
    --backdrop:#d6d6d8;
  }
  *{box-sizing:border-box;margin:0;padding:0}
  html,body{width:1200px;height:2303px;overflow:hidden;background:var(--backdrop)}
  .canvas{position:relative;width:1200px;height:2303px}
  .hanger{position:absolute;top:514px;width:520px;height:1274px;background:var(--white);overflow:hidden;box-shadow:0 14px 30px rgba(0,0,0,.22);font-family:"Montserrat",sans-serif;color:var(--ink)}
  .hanger--front{left:60px}
  .hanger--back{left:620px}
  .abs{position:absolute}
  .photo{position:absolute;left:0;width:100%}
  .photo--arena{top:0;height:600px;background:linear-gradient(180deg,#e9ebee 0%,#b9c3cc 35%,#8d9aa6 60%,#e2e5ea 80%,#5d6b7a 100%)}
  .photo--washer{top:0;height:600px;background:linear-gradient(135deg,#f1ece8 0%,#d39a78 35%,#b8643f 55%,#2f5f9e 75%,#233a5c 100%)}
  .photo--round{border-radius:50%;width:156px;height:156px;left:337px;top:683px;background:radial-gradient(circle at 40% 40%,#d9d6cf,#8d8a82 70%,#5a5650);border:4px solid var(--white)}
  .photo--before-after{top:720px;height:180px;background:linear-gradient(90deg,#8f9298 0%,#b7b9bd 50%,#c9cacb 100%)}
  .brand{position:absolute;display:flex;align-items:center;gap:12px;padding:0 22px;border-radius:12px;height:86px}
  .brand--dark{left:103px;top:300px;width:312px;background:rgba(13,42,79,.82);color:var(--white)}
  .brand--light{left:105px;top:292px;width:312px;background:rgba(255,255,255,.93);color:var(--navy)}
  .brand__mark{width:34px;height:34px;border-radius:50%;background:currentColor;flex:none}
  .brand__name{font-family:"Poppins",sans-serif;font-weight:700;font-size:22px;line-height:1.05}
  .band{position:absolute;left:0;width:520px}
  .why{position:absolute;left:30px;width:460px;top:566px;text-align:center;color:var(--white)}
  .why h2{font-family:"Poppins",sans-serif;font-weight:700;font-size:16px;margin-bottom:6px}
  .why p{font-size:10.8px;line-height:15.5px}
  .easy{position:absolute;left:44px;top:740px;font-family:"Sedgwick Ave Display",cursive;font-size:36px;color:var(--navy);letter-spacing:1px}
  .easy .num{color:var(--orange)}
  .easy .sep{color:var(--orange);font-size:20px;vertical-align:middle}
  .step{position:absolute;left:44px;width:446px;display:flex;gap:16px;align-items:flex-start}
  .step__icon{position:relative;flex:none;width:52px;height:52px;border-radius:50%;background:var(--orange);display:flex;align-items:center;justify-content:center}
  .step__num{position:absolute;left:-4px;top:-6px;width:18px;height:18px;border-radius:50%;background:var(--navy);color:var(--white);font-size:10px;font-weight:700;display:flex;align-items:center;justify-content:center}
  .step__text{font-size:12.4px;line-height:17.5px;padding-top:6px}
  .step__text b{font-weight:700}
  .studies{position:absolute;left:0;top:1035px;width:520px;height:150px;background:var(--panel);text-align:center;padding:24px 40px 0}
  .studies p{font-size:11.6px;line-height:17.5px}
  .studies p.lead{font-weight:700;font-size:13.4px;line-height:23px;margin-top:10px;color:var(--navy)}
  .phone{position:absolute;left:60px;top:1178px;width:400px;height:50px}
  .phone__text{position:absolute;inset:0;display:flex;align-items:center;justify-content:center;gap:8px;font-family:"Poppins",sans-serif;font-weight:700;font-size:34px;color:var(--white)}
  .footer{position:absolute;left:0;top:1226px;width:520px;height:48px;background:var(--navy);color:var(--white);display:flex;align-items:center;justify-content:center;gap:12px;font-family:"Poppins",sans-serif;font-weight:600;font-size:14.5px}
  .title{position:absolute;left:0;width:520px;text-align:center;font-family:"Sedgwick Ave Display",cursive;transform:rotate(-9deg)}
  .title--top{top:470px;font-size:84px;color:var(--orange);left:10px}
  .title--bottom{top:560px;font-size:84px;color:var(--white);left:14px}
  .tag{position:absolute;top:790px;height:30px;padding:0 12px;border-radius:15px;background:var(--orange);color:var(--white);font-family:"Poppins",sans-serif;font-weight:700;font-size:17px;display:flex;align-items:center;transform:rotate(-9deg)}
  .info{position:absolute;left:40px;width:440px;text-align:center}
  .info h3{font-family:"Poppins",sans-serif;font-weight:700;font-size:16.5px;color:var(--navy);margin-bottom:4px}
  .info p{font-size:11.6px;line-height:17.5px}
  .hole{position:absolute;left:0;top:0;pointer-events:none}
</style>
</head>
<body>
<main class="canvas">

  <!-- FRONT -->
  <section class="hanger hanger--front">
    <div class="photo photo--arena" role="img" aria-label="Harlow Dome arena facade with a Beacon Rinse &amp; Spray service truck parked in front"></div>

    <div class="brand brand--dark">
      <span class="brand__mark"></span>
      <span class="brand__name">Beacon Rinse &amp; Spray</span>
    </div>

    <svg class="band" style="top:460px" width="520" height="240" viewBox="0 0 520 240" aria-hidden="true">
      <path fill="#0d2a4f" d="M0 58 L30 52 L52 60 L78 46 L104 55 L140 40 L170 48 L205 35 L240 44 L270 30 L300 38 L330 22 L360 30 L385 14 L410 26 L440 8 L470 18 L495 2 L520 10 L520 196 L490 206 L470 198 L440 214 L410 204 L385 220 L350 210 L320 226 L290 214 L255 228 L225 216 L195 230 L160 218 L130 232 L100 220 L70 234 L40 222 L0 230 Z"/>
    </svg>

    <div class="why">
      <h2>Why is it important to remove graffiti quickly?</h2>
      <p>Graffiti tags are often viewed as ‘calling cards’ for the vandals that leave them. Simply put – one tag will encourage another, and another, and another to the same area. The best way to prevent graffiti is to quickly remove it. Removing it will also put you in compliance with Edmonton’s Community Standards Bylaw 14600 .</p>
    </div>

    <div class="photo--round abs" role="img" aria-label="Technician pressure washing graffiti off a concrete wall"></div>

    <div class="easy">Easy as <span class="num">1</span> <span class="sep">›</span> <span class="num">2</span> <span class="sep">›</span> <span class="num">3</span></div>

    <div class="step" style="top:818px">
      <div class="step__icon"><span class="step__num">1</span>
        <svg width="24" height="24" viewBox="0 0 24 24"><path fill="#fff" d="M6.6 10.8a15 15 0 0 0 6.6 6.6l2.2-2.2c.3-.3.7-.4 1-.2 1.1.4 2.3.6 3.6.6.6 0 1 .4 1 1V20c0 .6-.4 1-1 1A17 17 0 0 1 3 4c0-.6.4-1 1-1h3.5c.6 0 1 .4 1 1 0 1.3.2 2.5.6 3.6.1.3 0 .7-.2 1z"/></svg>
      </div>
      <p class="step__text" style="padding-top:14px">Call for a free quote - <b>780-555-0143</b></p>
    </div>

    <div class="step" style="top:880px">
      <div class="step__icon"><span class="step__num">2</span>
        <svg width="26" height="26" viewBox="0 0 24 24" fill="none" stroke="#fff" stroke-width="2"><circle cx="10" cy="10" r="6"/><path d="M14.5 14.5 20 20"/><path d="M7.5 10l2 2 3-3.5"/></svg>
      </div>
      <p class="step__text">Beacon Rinse &amp; Spray arrives <b>within 24 hrs</b> to identify the tag (examine the substrate &amp; surface ), provide quote, schedule removal of graffiti with <b>eco-friendly biodegradable</b> solutions &amp; pressure wash the area clean.</p>
    </div>

    <div class="step" style="top:976px">
      <div class="step__icon"><span class="step__num">3</span>
        <svg width="24" height="24" viewBox="0 0 24 24" fill="none" stroke="#fff" stroke-width="2"><rect x="3" y="5" width="18" height="14" rx="2"/><circle cx="9" cy="10" r="1.6" fill="#fff"/><path d="M4 17l5-5 4 4 3-3 4 4"/></svg>
      </div>
      <p class="step__text">Provide <b>before</b> and <b>after</b> photos documenting the removal of the graffiti.</p>
    </div>

    <div class="studies">
      <p>Studies have shown the best strategy for the prevention of further graffiti is immediate removal. The longer graffiti lingers, the more graffiti and vandalism it attracts.</p>
      <p class="lead">No matter what’s been put on your property it won’t be there for long when you Call Beacon Rinse &amp; Spray.</p>
    </div>

    <div class="phone">
      <svg width="400" height="50" viewBox="0 0 400 50" aria-hidden="true"><path fill="#f36f16" d="M8 6 L390 2 L384 12 L398 22 L386 32 L394 44 L12 48 L18 38 L2 28 L14 18 Z"/></svg>
      <div class="phone__text">
        <svg width="26" height="26" viewBox="0 0 24 24"><path fill="#fff" d="M6.6 10.8a15 15 0 0 0 6.6 6.6l2.2-2.2c.3-.3.7-.4 1-.2 1.1.4 2.3.6 3.6.6.6 0 1 .4 1 1V20c0 .6-.4 1-1 1A17 17 0 0 1 3 4c0-.6.4-1 1-1h3.5c.6 0 1 .4 1 1 0 1.3.2 2.5.6 3.6.1.3 0 .7-.2 1z"/></svg>
        780-555-0143
      </div>
    </div>

    <div class="footer"><span>beaconrinseandspray.ca</span><span>|</span><span>derek@beaconrinse.ca</span></div>

    <svg class="hole" width="520" height="260" viewBox="0 0 520 260" aria-hidden="true">
      <circle cx="262" cy="122" r="80" fill="#d6d6d8"/>
      <path fill="#d6d6d8" d="M320 70 C380 40 450 40 520 58 L520 74 C450 62 390 70 336 110 Z"/>
    </svg>
  </section>

  <!-- BACK -->
  <section class="hanger hanger--back">
    <div class="photo photo--washer" role="img" aria-label="Technician in a hi-vis vest steam washing a brick wall"></div>

    <div class="brand brand--light">
      <span class="brand__mark"></span>
      <span class="brand__name">Beacon Rinse &amp; Spray</span>
    </div>

    <div class="photo photo--before-after" role="img" aria-label="Before and after photo of a wall with graffiti tags removed"></div>

    <svg class="band" style="top:440px" width="520" height="320" viewBox="0 0 520 320" aria-hidden="true">
      <path fill="#0d2a4f" d="M0 80 L28 70 L50 78 L80 60 L110 66 L140 48 L175 54 L205 36 L240 42 L270 26 L300 32 L330 16 L362 22 L392 8 L420 14 L450 2 L485 10 L520 0 L520 230 L0 320 Z"/>
    </svg>

    <div class="title title--top">Graffiti</div>
    <div class="title title--bottom">Removal</div>

    <svg class="abs" style="left:220px;top:752px" width="100" height="40" viewBox="0 0 100 40" aria-hidden="true">
      <path d="M6 34 C20 4 60 -2 90 14" fill="none" stroke="#0d2a4f" stroke-width="3"/>
      <path d="M80 6 L92 15 L78 20" fill="none" stroke="#0d2a4f" stroke-width="3"/>
    </svg>
    <div class="tag" style="left:180px;top:800px">Before</div>
    <div class="tag" style="left:272px;top:784px">After</div>

    <svg class="band" style="top:820px" width="520" height="90" viewBox="0 0 520 90" aria-hidden="true">
      <path fill="#ffffff" d="M0 90 L0 80 L520 0 L520 90 Z"/>
      <path d="M0 84 L520 4" stroke="#0d2a4f" stroke-width="2" stroke-dasharray="14 8"/>
    </svg>

    <div class="info" style="top:876px">
      <h3>TRUSTED</h3>
      <p>Beacon Rinse &amp; Spray provides commercial graffiti removal services in the City of Edmonton &amp; Surrounding areas . We provide effective removal solutions for businesses affected by graffiti vandalism.</p>
    </div>

    <div class="info" style="top:962px">
      <h3>QUICK RESPONSE</h3>
      <p>We are here to help! Once we receive your call, Our team will arrange a site visit within 24 hrs to assess the surface, quote for the service, and then remove the graffiti. Beacon is committed to helping your business maintain a clean and professional property appearance. Your image matters to us!</p>
    </div>

    <div class="info" style="top:1084px">
      <h3>ABOUT US</h3>
      <p>We have been in business since 2011, providing power washing &amp; graffiti removal cleaning solutions. We are one of the largest Power washing companies within Edmonton!</p>
    </div>

    <div class="phone">
      <svg width="400" height="50" viewBox="0 0 400 50" aria-hidden="true"><path fill="#f36f16" d="M8 6 L390 2 L384 12 L398 22 L386 32 L394 44 L12 48 L18 38 L2 28 L14 18 Z"/></svg>
      <div class="phone__text">
        <svg width="26" height="26" viewBox="0 0 24 24"><path fill="#fff" d="M6.6 10.8a15 15 0 0 0 6.6 6.6l2.2-2.2c.3-.3.7-.4 1-.2 1.1.4 2.3.6 3.6.6.6 0 1 .4 1 1V20c0 .6-.4 1-1 1A17 17 0 0 1 3 4c0-.6.4-1 1-1h3.5c.6 0 1 .4 1 1 0 1.3.2 2.5.6 3.6.1.3 0 .7-.2 1z"/></svg>
        780-555-0143
      </div>
    </div>

    <div class="footer"><span>beaconrinseandspray.ca</span><span>|</span><span>derek@beaconrinse.ca</span></div>

    <svg class="hole" width="520" height="260" viewBox="0 0 520 260" aria-hidden="true">
      <circle cx="262" cy="122" r="80" fill="#d6d6d8"/>
      <path fill="#d6d6d8" d="M204 66 C150 40 70 40 0 58 L0 74 C70 62 130 70 188 110 Z"/>
    </svg>
  </section>

</main>
</body>
</html>
```